Filmproduktion braucht Visitenkarten und Briefpapier
Zielgruppe
Wir sind eine junge Filmproduktion Firma mit dem Namen Lichtkante.
Unser Kerngeschäft sind Image und Unternehmensfilme, sowie Event und Messefilme.
Aufgabenstellung
Wir sind junge, kreative, Filmschaffende und das soll sich auch in der Visitenkarte widerspiegeln, dennoch macht bitte auch ein paar klassische Vorschläge, manchmal ist weniger mehr.
Unser altes Briefpapier ist angehängt. Das neue Briefpapier muss von uns veränderbar sein, da wir noch nicht alle Daten haben wie Steuernummer und USt-ID, bitte aber schon als Dummy anlegen.
Unsere alten Visitenkarten sind angehängt, diese Daten Stimmen, aber ansonsten stimmt daran nix, wie wir finden. Bitte nicht daran Orientieren!!!
Bitte bei der Adresse Lichtkante GbR schreiben.
Unser neues Logo, jetzt in blau ist ebenfalls angehängt.
Viel Spass beim Designen.

```html
<!DOCTYPE html>
<html lang="de">
<head>
<meta charset="utf-8">
<title>Lichtkante – Briefpapier und Visitenkarten</title>
<link href="https://fonts.googleapis.com/css2?family=Lato:wght@400;700&family=Oswald:wght@300;400&display=swap" rel="stylesheet">
<style>
  :root {
    --bg: #e4e2e2;
    --paper: #f4f4f5;
    --blue: #2f7fc4;
    --blue-light: #4a9be0;
    --blue-pale: #cfdbe6;
    --navy: #1c2f6b;
    --ink: #3b3b3b;
    --grey: #8a8a8a;
  }
  * { box-sizing: border-box; margin: 0; padding: 0; }
  html, body { width: 1200px; height: 1029px; overflow: hidden; }
  body { background: var(--bg); font-family: "Lato", sans-serif; color: var(--ink); position: relative; }

  .letterhead { position: absolute; left: 203px; top: 159px; width: 505px; height: 734px; background: var(--paper); box-shadow: 0 1px 3px rgba(0,0,0,.12); }
  .letterhead > * { position: absolute; }
  .top-band { left: 3px; right: 3px; top: 5px; height: 9px; background: linear-gradient(90deg, #d6dde4, #c9d6e3, #d6dde4); }
  .web-bar { left: 379px; top: 18px; width: 126px; height: 12px; background: var(--blue); color: #fff; font-weight: 700; font-size: 7px; letter-spacing: 1.3px; text-align: center; line-height: 12px; }
  .brand { left: 118px; top: 98px; display: flex; align-items: center; gap: 5px; font-size: 14px; font-weight: 700; color: var(--ink); }
  .brand .dot { width: 9px; height: 9px; border-radius: 50%; background: var(--blue); }
  .sender { left: 61px; top: 130px; font-size: 7px; }
  .sender b { color: var(--blue); font-weight: 400; }
  .recipient { left: 61px; top: 148px; font-size: 6px; line-height: 9px; }
  .contact { left: 379px; display: flex; gap: 11px; font-size: 6px; line-height: 11px; }
  .contact .icon { width: 20px; height: 20px; background: var(--blue); display: flex; align-items: center; justify-content: center; }
  .c1 { top: 90px; } .c2 { top: 126px; } .c3 { top: 161px; }
  .subject { left: 61px; top: 252px; font-size: 11px; line-height: 16px; }
  .subject .s1 { color: var(--blue); font-weight: 700; }
  .subject .s2 { color: #555; }
  .date-bar { left: 52px; top: 285px; width: 118px; height: 12px; background: linear-gradient(90deg, var(--blue) 70%, #7fb0de); color: #fff; font-size: 7px; line-height: 12px; padding-left: 9px; }
  .body-text { left: 61px; width: 385px; font-size: 6.4px; line-height: 17.6px; color: #555; }
  .p1 { top: 319px; } .p2 { top: 406px; } .p3 { top: 475px; }
  .signature { left: 70px; top: 565px; width: 90px; height: 28px; background: linear-gradient(90deg, transparent, #dcdde0, transparent); }
  .sign-line { left: 106px; top: 597px; width: 116px; height: 1px; background: #999; left: 105px; }
  .sign-role { left: 59px; top: 601px; font-size: 5.5px; line-height: 8px; color: var(--blue); }
  .sign-role span { color: #aaa; display: block; }
  .sign-line { left: 105px; }
  .footer { top: 690px; font-size: 5.5px; line-height: 11px; color: var(--grey); }
  .footer b { color: var(--blue); font-weight: 400; }
  .f1 { left: 59px; } .f2 { left: 200px; }
  .bottom-band { left: 0; right: 8px; top: 724px; height: 8px; background: linear-gradient(90deg, var(--blue), var(--blue-light), var(--blue)); }

  .card { position: absolute; left: 759px; width: 229px; height: 140px; background: var(--navy); box-shadow: 0 1px 3px rgba(0,0,0,.2); }
  .card-front { top: 157px; }
  .card-back { top: 337px; }
  .card .pattern { position: absolute; inset: 0; background: linear-gradient(135deg, #1d4f8e, #2a78c2 55%, #1d3f7a); opacity: .55; }
  .card-front .panel { position: absolute; left: 15px; top: 15px; width: 199px; height: 110px; background: linear-gradient(160deg, #2f8ed8, #1f6fc0); display: flex; align-items: center; justify-content: center; gap: 18px; }
  .vertical { writing-mode: vertical-rl; }
  .front-name { color: #fff; font-size: 7px; letter-spacing: 5px; font-weight: 400; }
  .front-dot { width: 18px; height: 18px; border-radius: 50%; background: #fff; }
  .card-back .panel { position: absolute; left: 15px; top: 14px; width: 200px; height: 111px; background: #f7f8fa; border-radius: 3px; display: flex; flex-direction: row-reverse; align-items: center; justify-content: flex-start; gap: 9px; padding-right: 14px; }
  .back-brand { font-size: 5.5px; letter-spacing: 4px; color: #333; }
  .back-dot { width: 9px; height: 9px; border-radius: 50%; background: var(--blue); }
  .name-pill { font-family: "Oswald", sans-serif; font-weight: 300; font-size: 13px; color: #333; border: 1.5px solid var(--blue-light); border-radius: 5px; padding: 6px 3px; }
  .phone-pill { font-family: "Oswald", sans-serif; font-weight: 300; font-size: 12px; color: #fff; background: var(--blue-light); border-radius: 5px; padding: 6px 3px; }
  .back-info { font-size: 4.3px; line-height: 7px; color: #555; }
  .back-info b { color: var(--blue); font-weight: 400; }
</style>
</head>
<body>

<section class="letterhead" aria-label="Briefpapier">
  <div class="top-band"></div>
  <div class="web-bar">www.lichtkante.example</div>
  <div class="brand"><span class="dot"></span>Lichtkante</div>
  <p class="sender"><b>LICHTKANTE GbR</b> • Lindenhof 7 • 10115 Berlin</p>
  <p class="recipient">Herrn<br>Vincent Mustermann<br>Max Musterstraße 2<br>24143 Musterburg</p>

  <div class="contact c1">
    <span class="icon"><svg width="11" height="11" viewBox="0 0 12 12" fill="none" stroke="#fff" stroke-width="1"><circle cx="6" cy="6" r="5"/><ellipse cx="6" cy="6" rx="2.2" ry="5"/><path d="M1 6h10"/></svg></span>
    <p>www.lichtkante.example<br>mail@lichtkante.example</p>
  </div>
  <div class="contact c2">
    <span class="icon"><svg width="8" height="12" viewBox="0 0 8 12"><rect x="1" y="0.5" width="6" height="11" rx="1" fill="#fff"/><rect x="2" y="2" width="4" height="5" fill="#2f7fc4"/></svg></span>
    <p>0300 4417 20<br>0300 4417 21</p>
  </div>
  <div class="contact c3">
    <span class="icon"><svg width="11" height="10" viewBox="0 0 12 11"><path d="M6 0L0 5.5h2V11h3V7.5h2V11h3V5.5h2z" fill="#fff"/></svg></span>
    <p>Lindenhof 7<br>10115 Berlin</p>
  </div>

  <div class="subject"><p class="s1">Lorem</p><p class="s2">Ipsum Dolor</p></div>
  <div class="date-bar">21.10.2013</div>

  <p class="body-text p1">Ut dapibus, turpis quis lacinia cursus, risus ante cursus risus, vel luctus erat magna a ligula. Phasellus vulputate sapien orci, sed bibendum nisl. Cras dignissim, sapien ac cursus commodo, elit magna vulputate tellus, id sagittis enim dolor nec felis. Aliquam ornare lorem ut ipsum ullamcorper commodo. Curabitur tristique rutrum erat, iaculis laoreet libero sagittis non.</p>
  <p class="body-text p2">Sed quis diam felis. Ut a sapien vitae eros feugiat feugiat. Vivamus pulvinar commodo cursus. Etiam vulputate vulputate justo, et fermentum orci convallis non. Maecenas elit odio, gravida in congue et, porta sed ipsum. Morbi quis ligula nec nulla posuere lobortis vel et dolor. Ut neque dui, sollicitudin id gravida ut, fermentum ac nibh.</p>
  <p class="body-text p3">Mauris rutrum velit tincidunt dolor tristique ac adipiscing odio auctor. Cras leo magna, ultrices volutpat egestas ut, pellentesque eget purus. Fusce fringilla, metus et congue eleifend, ligula eros viverra nibh, sit amet placerat eros justo sed libero. Ut feugiat ligula sed nisi condimentum tempus. Ut eu libero purus, luctus blandit felis. Phasellus in diam ipsum, vitae tempus odio. Nullam pellentesque mauris in ligula consectetur.</p>

  <div class="signature" role="img" aria-label="Platz für die handschriftliche Unterschrift"></div>
  <div class="sign-line" style="left:45px;width:120px"></div>
  <p class="sign-role">GESCHÄFTSFÜHRER<span>LICHTKANTE GbR</span></p>

  <p class="footer f1">IBAN: <b>DE00 1234 5678 0000 1111 22</b><br>BIC/SWIFT-Code: <b>MUSTDEXXXXX</b></p>
  <p class="footer f2">Umsatzsteuer ID: <b>DE 000000000</b><br>Steuernummer: <b>00/000/00000</b></p>
  <div class="bottom-band"></div>
</section>

<section class="card card-front" aria-label="Visitenkarte Vorderseite">
  <div class="pattern" role="img" aria-label="Rasterfläche aus blauen Quadraten"></div>
  <div class="panel">
    <span class="front-dot"></span>
    <p class="vertical front-name">LICHTKANTE</p>
  </div>
</section>

<section class="card card-back" aria-label="Visitenkarte Rückseite">
  <div class="pattern" role="img" aria-label="Rasterfläche aus blauen Quadraten"></div>
  <div class="panel">
    <span class="back-dot"></span>
    <p class="vertical back-brand">LICHTKANTE</p>
    <p class="vertical name-pill">JONAS BREHM</p>
    <p class="vertical phone-pill">0151 - 40 33 17 08</p>
    <p class="vertical back-info">Lichtkante - Filmproduktion<br>Lichtkante GbR, 10115 Berlin<br><b>brehm@lichtkante.example</b><br><b>www.lichtkante.example</b></p>
  </div>
</section>

</body>
</html>
```